eBook Cover

Here is the book title: 27 LESSONS EACH MINISTER SHOULD
LEARN ABOUT FINANCES

Here is the subtitle (or author section): A Harvest Lantern eBook

I've attached the harvest lantern logo below.

Target Market(s)

Church Pastors

Requirements
Must have
• Lantern Logo and Harvest Lantern color palette.
Nice to have
• I have attached some sample book covers that I like

```html
<!DOCTYPE html>
<html lang="en">
<head>
<meta charset="utf-8">
<title>27 Lessons Each Minister Should Learn About Finances – A Harvest Lantern eBook</title>
<link rel="stylesheet" href="https://fonts.googleapis.com/css2?family=Bebas+Neue&family=Oswald:wght@500&display=swap">
<style>
  :root {
    --band: #000000;
    --brand-grey: #8c8c8c;
    --header-text: #e2e2e2;
    --yellow-deep: #f7bf00;
    --yellow-mid: #fcd23a;
    --yellow-glow: #fff1b8;
    --title: #ffffff;
    --ink: #000000;
  }
  * { margin: 0; padding: 0; box-sizing: border-box; }
  html, body { width: 800px; height: 1200px; overflow: hidden; background: var(--yellow-deep); }
  .cover {
    position: relative;
    width: 800px;
    height: 1200px;
    overflow: hidden;
    background:
      radial-gradient(ellipse 420px 300px at 50% 900px, var(--yellow-glow) 0%, var(--yellow-mid) 45%, rgba(252,210,58,0) 100%),
      linear-gradient(180deg, var(--yellow-deep) 0%, var(--yellow-mid) 70%, var(--yellow-deep) 100%);
    font-family: "Bebas Neue", "Arial Narrow", sans-serif;
  }
  .top-band {
    position: absolute;
    left: 0; top: 0;
    width: 800px; height: 137px;
    background: var(--band);
    display: flex;
    align-items: center;
    justify-content: space-between;
    padding: 0 36px 0 22px;
  }
  .publisher {
    display: flex;
    align-items: center;
    gap: 8px;
  }
  .publisher-mark {
    width: 14px;
    height: 14px;
    border-radius: 50%;
    background: var(--brand-grey);
  }
  .publisher-name {
    color: var(--brand-grey);
    font-family: "Bebas Neue", "Arial Narrow", sans-serif;
    font-size: 26px;
    line-height: 1;
    letter-spacing: 1px;
    white-space: nowrap;
  }
  .series-label {
    color: var(--header-text);
    font-family: "Oswald", "Arial Narrow", sans-serif;
    font-weight: 500;
    font-size: 50px;
    letter-spacing: 0.5px;
    white-space: nowrap;
  }
  .title-line {
    position: absolute;
    left: 0;
    width: 800px;
    text-align: center;
    color: var(--title);
    line-height: 1;
    white-space: nowrap;
  }
  .title-small { font-size: 104px; letter-spacing: 1px; }
  .title-large { font-size: 234px; letter-spacing: 0; }
  .line-one { top: 180px; }
  .line-two { top: 264px; }
  .line-three { top: 475px; }
  .line-four { top: 562px; }
  .cross-letter {
    display: inline-block;
    height: 0.7em;
    width: 0.38em;
    vertical-align: baseline;
    margin: 0 0.01em;
  }
  .bill-photo {
    position: absolute;
    left: 215px;
    top: 840px;
    width: 380px;
    height: 150px;
    transform: rotate(-8deg) skewX(12deg);
    background: linear-gradient(135deg, #c9cdb6 0%, #aab29a 50%, #8f9a7f 100%);
    box-shadow: 0 6px 12px rgba(150,110,0,0.25);
  }
  .author-name {
    position: absolute;
    left: 0;
    top: 1088px;
    width: 800px;
    text-align: center;
    color: var(--ink);
    font-size: 84px;
    line-height: 1;
    letter-spacing: 1px;
  }
</style>
</head>
<body>
  <main class="cover">
    <header class="top-band">
      <div class="publisher">
        <span class="publisher-mark" aria-hidden="true"></span>
        <span class="publisher-name">The Lantern Company</span>
      </div>
      <div class="series-label">A Harvest Lantern eBook</div>
    </header>

    <h1 class="book-title" aria-label="27 Lessons Each Minister Should Learn About Finances">
      <span class="title-line title-small line-one">27 Lessons Each</span>
      <span class="title-line title-large line-two">MINIS<svg class="cross-letter" viewBox="0 0 76 140" aria-hidden="true"><rect x="24" y="0" width="28" height="140" fill="#000"/><rect x="0" y="30" width="76" height="26" fill="#000"/></svg>ER</span>
      <span class="title-line title-small line-three">Should Learn About</span>
      <span class="title-line title-large line-four">Finances</span>
    </h1>

    <div class="bill-photo" role="img" aria-label="Photograph of a one-dollar bill lying flat on the yellow surface"></div>

    <p class="author-name">Author Name</p>
  </main>
</body>
</html>
```